Emerging Ed-Tech Startup seeking Stationery Designs!

We are in need of basic set of stationery designs to be used for our business operations, letters, emails, and in-office materials. We are a technology startup enhancing on campus work experience offerings by establishing a collaborative work environment for the completion of such tasks.

Our colors are Vibrant Tiffany Blue/Black/White.

Website: www.scholarhorizonhub.com (Still under construction aside from the landing pages)

Please make sure the designs use a brighter more vibrant tiffany blue color than seen in the image files uploaded. We are not using those materials.

Our logo has been added as a file as well, please use that for any designs (include that logo). Thank you.

```html
<!DOCTYPE html>
<html lang="en">
<head>
<meta charset="utf-8">
<title>ScholarHorizon Business Card</title>
<link href="https://fonts.googleapis.com/css2?family=Arimo:wght@400;700&display=swap" rel="stylesheet">
<style>
  :root {
    --tiffany: #1fe3c8;
    --tiffany-soft: #8ff2e3;
    --mint-pale: #dcfbf5;
    --ink: #111111;
    --charcoal: #444444;
    --text-grey: #7a7a7a;
    --paper: #ffffff;
    --edge: #9a9a9a;
  }
  html, body {
    margin: 0;
    padding: 0;
    width: 1200px;
    height: 684px;
    overflow: hidden;
    background: var(--paper);
  }
  .card {
    position: relative;
    width: 1200px;
    height: 684px;
    box-sizing: border-box;
    border: 2px solid var(--edge);
    background: var(--paper);
    overflow: hidden;
    font-family: "Arimo", Arial, sans-serif;
  }
  .card__waves {
    position: absolute;
    inset: 0;
    width: 100%;
    height: 100%;
  }
  .brand {
    position: absolute;
    left: 50px;
    top: 46px;
    display: flex;
    align-items: center;
    gap: 22px;
  }
  .brand__square {
    width: 138px;
    height: 138px;
    background: var(--tiffany);
  }
  .brand__name {
    font-size: 46px;
    font-weight: 400;
    color: var(--charcoal);
    letter-spacing: 1px;
  }
  .person {
    position: absolute;
    right: 54px;
    top: 46px;
    text-align: right;
  }
  .person__name {
    margin: 0;
    font-size: 39px;
    font-weight: 700;
    color: var(--ink);
    letter-spacing: 0.5px;
  }
  .person__role,
  .person__phone {
    margin: 14px 0 0;
    font-size: 28px;
    color: var(--text-grey);
  }
  .contact {
    position: absolute;
    left: 50px;
    top: 366px;
    font-size: 28px;
    line-height: 39px;
    color: var(--text-grey);
  }
  .contact p { margin: 0; }
  .contact__sep { margin: 0 14px; }
  .contact__web { color: var(--tiffany); }
</style>
</head>
<body>
<div class="card">
  <svg class="card__waves" viewBox="0 0 1200 684" preserveAspectRatio="none" aria-hidden="true">
    <path d="M0,600 C300,560 620,600 900,684 L0,684 Z" fill="var(--mint-pale)"/>
    <path d="M1200,250 C1100,420 900,570 640,684 L1200,684 Z" fill="var(--charcoal)"/>
    <path d="M1200,400 C1050,520 800,610 430,684 L1200,684 Z" fill="var(--tiffany-soft)" opacity="0.85"/>
    <path d="M1200,500 C1080,580 920,640 760,684 L1200,684 Z" fill="var(--tiffany)"/>
  </svg>

  <div class="brand">
    <div class="brand__square"></div>
    <span class="brand__name">ScholarHorizon</span>
  </div>

  <div class="person">
    <p class="person__name">MR. OWEN CARTER</p>
    <p class="person__role">Marketing Manager</p>
    <p class="person__phone">+91 14 5583017</p>
  </div>

  <div class="contact">
    <p>House # B-14<span class="contact__sep">|</span>Lake Avenue<span class="contact__sep">|</span></p>
    <p>+91 27 4418390<span class="contact__sep">|</span>info@scholarhorizonhub.com<span class="contact__sep">|</span></p>
    <p class="contact__web">www.scholarhorizonhub.com</p>
  </div>
</div>
</body>
</html>
```